Brightwell Bonds and Households Initiative

We need a flyer that invites low-income Spanish speaking individuals to our program. The program is 12 weeks. We offer healthy relationship education, and financial stability. We also touch on workforce development. These workshops are for couples only.

We are in five locations, so we need a flyer that we can change the text to be able to update the address, dates and any additional information based on our needs.

Attached is the logo we would like to use. I have also attached a previous flyer that we created to give you an idea of the text that is included.

Target Market(s)

We are reaching out to low income adult couples

Font styles to use
Serif

Requirements
Must have
• This flyer must catch the eye of couples wanting to improve their relationship, and finances.
Nice to have
• Some space for us to plug in dates location and times. This flyer also has to have our funding statement at the bottom.

```html
<!DOCTYPE html>
<html lang="es">
<head>
<meta charset="utf-8">
<title>Talleres para Parejas</title>
<link rel="stylesheet" href="https://fonts.googleapis.com/css2?family=Noto+Serif:ital,wght@0,400;0,600;0,700;0,800;1,400;1,700&display=swap">
<style>
  :root{
    --navy:#1f3f73;
    --blue:#1e6fb8;
    --orange:#f39a1f;
    --orange-deep:#ea7a12;
    --panel:#eeeeef;
    --panel-dark:#e2e3e5;
    --text:#3b3b3b;
    --white:#ffffff;
  }
  *{box-sizing:border-box;margin:0;padding:0}
  html,body{width:1200px;height:1084px;overflow:hidden;background:var(--white)}
  body{font-family:"Noto Serif",Georgia,serif;color:var(--text);position:relative}
  .flyer{position:absolute;inset:0;background:var(--white)}
  .top-strip{position:absolute;left:0;top:0;width:468px;height:10px;background:var(--orange)}
  .brand{position:absolute;left:40px;top:60px;width:400px;display:flex;align-items:center;gap:14px}
  .brand-dot{width:46px;height:46px;border-radius:50%;background:var(--orange);flex:none}
  .brand-name{font-size:20px;font-weight:700;color:var(--navy);line-height:1.25}
  .title{position:absolute;left:40px;top:204px;width:420px;font-size:27px;font-weight:800;color:var(--navy);white-space:nowrap}
  .photo{position:absolute;left:468px;top:0;width:732px;height:420px;
    background:linear-gradient(160deg,#f7b646 0%,#f59c2c 35%,#e8c38c 60%,#b9b4ae 85%,#8a8986 100%)}
  .tagline{position:absolute;left:24px;top:262px;width:500px;height:72px;background:var(--blue);color:var(--white);
    text-align:center;padding-top:8px;font-size:18px;line-height:1.3;z-index:2}
  .tagline strong{display:block;font-size:23px;font-style:italic;font-weight:700}
  .tagline .q{color:var(--orange);font-style:normal}
  .dates{position:absolute;left:40px;top:350px;width:420px}
  .dates h3{font-size:26px;font-weight:700;color:var(--orange-deep);line-height:1.2}
  .dates p{font-size:22px;font-weight:700;color:var(--navy);white-space:nowrap}
  .topics{position:absolute;left:0;top:430px;width:550px;height:350px;background:var(--panel);padding:20px 40px}
  .topics h3{font-size:26px;font-weight:700;color:var(--navy);margin-bottom:8px}
  .topics ul{list-style:none}
  .topics li{font-size:17px;line-height:1.55;color:var(--text);display:flex;align-items:center;gap:12px}
  .topics li::before{content:"";width:11px;height:11px;border-radius:50%;background:var(--orange);flex:none}
  .side{position:absolute;left:550px;top:420px;width:650px;height:664px;background:var(--panel-dark);padding:40px 50px}
  .side h3{font-size:28px;font-weight:700;color:var(--orange-deep);line-height:1.25}
  .side .val{font-size:28px;color:var(--text);margin-bottom:36px}
  .side .addr{font-size:21px;color:var(--text);line-height:1.4;margin-bottom:22px}
  .side .phone{font-size:30px;font-weight:700;color:var(--navy);display:flex;align-items:center;gap:12px}
  .partners{margin-top:34px;display:flex;flex-direction:column;gap:22px;align-items:flex-start}
  .partner{display:flex;align-items:center;gap:12px;font-size:19px;font-weight:700;color:var(--navy)}
  .partner .mark{width:38px;height:38px;background:var(--orange);flex:none}
  .partner .mark.round{border-radius:50%;background:#b3262d}
  .register{position:absolute;left:24px;top:790px;width:516px;height:112px;background:var(--blue);color:var(--white);padding:8px 24px}
  .register p{font-size:26px;font-weight:600}
  .register h2{font-size:46px;font-weight:800;color:var(--white);line-height:1.1}
  .info{position:absolute;left:40px;top:916px;font-size:16px;line-height:1.35;color:var(--text)}
  .info strong{color:var(--navy)}
  .funding{position:absolute;left:30px;top:994px;width:505px;font-size:12px;line-height:1.35;font-style:italic;color:var(--text);padding-left:22px}
  .funding .mark-q{position:absolute;left:0;top:-8px;font-size:32px;font-weight:800;color:var(--orange);font-style:normal}
  .bottom-strip{position:absolute;left:0;bottom:0;width:550px;height:10px;background:var(--orange)}
</style>
</head>
<body>
<div class="flyer">
  <div class="top-strip"></div>

  <div class="brand">
    <span class="brand-dot"></span>
    <span class="brand-name">Brightwell Bonds and Households Initiative</span>
  </div>

  <h1 class="title">TALLERES PARA PAREJAS</h1>

  <div class="photo" role="img" aria-label="Fotografía de una pareja abrazada frente a un atardecer en la playa"></div>

  <div class="tagline">
    Porque una relación sana está
    <strong><span class="q">“</span> A Nuestro Alcance <span class="q">”</span></strong>
  </div>

  <div class="dates">
    <h3>Fecha de talleres:</h3>
    <p>jueves octubre 03, 12, 19, 26</p>
  </div>

  <section class="topics">
    <h3>Temas incluyen:</h3>
    <ul>
      <li>Llaves para la buena comunicación</li>
      <li>Tipos de personalidad y preguntas clave</li>
      <li>Señales de peligro en una relación</li>
      <li>Técnicas para formar y sostener una relación duradera</li>
      <li>Resolución de problemas</li>
      <li>Como mantener la diversión</li>
      <li>Como administrar el dinero entre pareja</li>
      <li>Y mucho más</li>
    </ul>
  </section>

  <aside class="side">
    <h3>Horario:</h3>
    <p class="val">5:30pm –8:00pm</p>
    <h3>Ubicación:</h3>
    <p class="addr">Linden Grove Family<br>Resource Center<br>2760 Linden Ave. Fairhaven, CA 90410</p>
    <p class="phone">
      <svg width="28" height="28" viewBox="0 0 24 24" aria-hidden="true"><path fill="#1f3f73" d="M6.6 10.8a15.1 15.1 0 0 0 6.6 6.6l2.2-2.2a1 1 0 0 1 1-.25 11.4 11.4 0 0 0 3.6.57 1 1 0 0 1 1 1V20a1 1 0 0 1-1 1A17 17 0 0 1 3 4a1 1 0 0 1 1-1h3.5a1 1 0 0 1 1 1c0 1.25.2 2.45.57 3.57a1 1 0 0 1-.25 1z"/></svg>
      (555) 201-4480
    </p>
    <div class="partners">
      <div class="partner"><span class="mark"></span>Linden Grove Family Resource Center</div>
      <div class="partner"><span class="mark round"></span>Harbor Partners Network</div>
    </div>
  </aside>

  <div class="register">
    <p>Registración requerida</p>
    <h2>Llámanos hoy!</h2>
  </div>

  <p class="info">Para más información llame a<br><strong>Linden Grove Family Resource Center</strong><br><strong>(555) 201-4492</strong></p>

  <p class="funding"><span class="mark-q">“</span>Funding for this project was provided by the Office of Family Strength Grants, Award #00XX0000. These services are available to all eligible persons, regardless of race, gender, age, disability, or religion.</p>

  <div class="bottom-strip"></div>
</div>
</body>
</html>
```